BRASSWELL TARGET SPORTS, A modern indoor gun range comfortable for anyone to visit.

Please note the attached "Operating Plan", and "Letter of Introduction" for more details on our operation.

What we are looking for is the overall feel and look of the website. A lot of the details in how many links, what links, etc we will have built later. It's more important we get the right color scheme, flow, feel, etc.

This is an indoor gun range in Colorado. We are looking to be the fun lanes of the gun industry. We want a website that is simple, but stylish. Our range is forward thinking and modern. Please see our logo attached.

Our indoor range will also have a small cafe that will sell coffee, mixed soda drinks, and made from scratch cinnamon rolls.

Our look will be lighter colors. We want to avoid anything that would seem aggressive. Simple is the key here. We love simple clean designs. Pixel parlor has a good look and feel to it. Something with the same feel would be great. Our logo is red and black; however, we don't want the website to be dominated by those colors. Blue is also a great color.

We need a landing page that can shrink to different sizes of screens.
No mobile format.
Contact page with email submission
Menu will only have a couple links. We are open to different formats. Fun lanes format is also a good design.

Possible links will include: Home, Membership, About Us, Contact Us, Classes, Cafe

Target Market(s)

Primary target is male 35-55 years old with some college or more.

Number of Pages Required

3 page

Font styles to use
Sans Serif

Colors

Designer to choose colors to be used in the design.

Requirements
Must have
• Page 1 Landing first page
• Page 2 Blog posts to give updates on building progress
• Page 3 About us (hours of operation, etc)

```html
<!DOCTYPE html>
<html lang="en">
<head>
<meta charset="utf-8">
<title>Brasswell Target Sports</title>
<link rel="stylesheet" href="https://fonts.googleapis.com/css2?family=Montserrat:wght@300;400;700;800&family=Lato:wght@400;700&display=swap">
<style>
:root{
  --red:#d2232a;
  --ink:#1b1b1b;
  --text:#555;
  --muted:#777;
  --pink-line:#f1b9bf;
  --pink-bg:#fce9ea;
  --grey-band:#f2f2f2;
  --blue:#5ec0ea;
  --blue-text:#4fb6e8;
  --salmon:#f9a78a;
  --white:#fff;
}
*{box-sizing:border-box;margin:0;padding:0}
html,body{width:1200px;height:3582px;overflow:hidden}
body{position:relative;background:var(--white);font-family:'Lato',sans-serif;color:var(--text)}
.abs{position:absolute}

/* header */
.site-header{left:0;top:0;width:1200px;height:108px;background:var(--white);border-bottom:1px solid #e6e6e6}
.brand{display:flex;align-items:center;gap:12px}
.brand-dot{width:16px;height:16px;border-radius:50%;background:var(--red);flex:none}
.brand-name{font-family:'Montserrat',sans-serif;font-weight:800;color:var(--ink);line-height:1.05;letter-spacing:.5px}
.header-brand{left:146px;top:26px}
.header-brand .brand-name{font-size:19px}
.phone-bar{left:688px;top:0;width:512px;height:49px;background:#fdeeee;clip-path:polygon(0 0,100% 0,100% 100%,40px 100%);display:flex;align-items:center;padding-left:60px;font-family:'Lato',sans-serif;font-size:20px;color:var(--ink)}
.phone-bar svg{margin-right:8px}
.phone-bar b{font-weight:700;font-size:24px;margin-left:6px}
.main-nav{left:418px;top:70px;display:flex;gap:32px;font-family:'Lato',sans-serif;font-size:15px;color:var(--ink);align-items:center}
.main-nav .active{color:var(--red)}

/* hero */
.hero{left:0;top:108px;width:1200px;height:615px;overflow:hidden}
.hero-photo{width:100%;height:100%;background:linear-gradient(100deg,#2b2522 0%,#5a4a40 35%,#8a8079 60%,#c9c5c1 100%)}
.hero-title{left:663px;top:152px;font-family:'Montserrat',sans-serif;font-weight:800;font-size:62px;line-height:72px;color:var(--white);letter-spacing:1px}
.btn-outline-light{left:663px;top:401px;width:172px;height:44px;border:2px solid var(--white);border-radius:22px;background:rgba(0,0,0,.35);color:var(--white);font-size:15px;font-weight:700;display:flex;align-items:center;justify-content:center;gap:6px}
.carousel-arrow{top:236px;width:40px;height:40px;border-radius:50%;background:#111;display:flex;align-items:center;justify-content:center}
.dots{left:553px;display:flex;gap:10px}
.dots span{width:10px;height:10px;border-radius:50%;background:var(--white)}
.dots span.on{background:transparent;border:2px solid var(--white)}
.hero-curve{left:0;top:600px}
.hero-badge{left:571px;top:694px;width:58px;height:58px;border-radius:50%;background:var(--white);border:3px solid var(--red)}

/* headings */
.section-title{font-family:'Montserrat',sans-serif;font-size:42px;color:var(--ink);letter-spacing:1px}
.section-title b{font-weight:800}
.section-title span{font-weight:300}
.title-rule{height:2px;background:var(--pink-line)}
.btn-read{height:46px;border:1px solid #ccc;border-radius:23px;background:var(--white);box-shadow:0 2px 4px rgba(0,0,0,.15);color:var(--red);font-weight:700;font-size:15px;display:flex;align-items:center;justify-content:center;gap:6px}

/* welcome */
.welcome-emblem{left:180px;top:820px;width:320px;height:380px;display:flex;align-items:center;justify-content:center}
.welcome-emblem div{width:330px;height:330px;border-radius:50%;background:radial-gradient(circle,#f6f6f6 0%,#ececec 100%)}
.welcome-title{left:577px;top:815px;font-family:'Montserrat',sans-serif;font-weight:800;font-size:40px;color:var(--ink)}
.welcome-sub{left:577px;top:870px;font-family:'Montserrat',sans-serif;font-weight:300;font-size:29px;color:var(--ink);letter-spacing:.5px}
.welcome-rule{left:577px;top:924px;width:366px}
.welcome-copy{left:577px;top:948px;width:460px;font-size:14px;line-height:31px;color:var(--muted)}
.welcome-btn{left:577px;top:1134px;width:163px}

/* membership */
.membership{left:0;top:1332px;width:1200px;height:549px;background:var(--grey-band)}
.membership-top{left:0;top:1268px}
.membership-bottom{left:0;top:1880px}
.membership-title{left:0;top:1350px;width:1200px;text-align:center}
.membership-rule{left:418px;top:1418px;width:365px}
.plan{top:1471px;width:436px;height:208px;background:var(--white);box-shadow:0 2px 6px rgba(0,0,0,.12);overflow:hidden}
.plan-yearly{left:149px}
.plan-monthly{left:614px}
.price-panel{position:absolute;left:0;top:0;width:190px;height:208px;border-radius:0 50% 50% 0/0 50% 50% 0;display:flex;flex-direction:column;align-items:center;justify-content:center;color:var(--white);text-align:center}
.price-panel.blue{background:var(--blue);box-shadow:8px 0 0 rgba(94,192,234,.25)}
.price-panel.salmon{background:var(--salmon);box-shadow:8px 0 0 rgba(249,167,138,.25)}
.price-amount{font-family:'Montserrat',sans-serif;font-weight:700;font-size:52px;line-height:1}
.price-label{font-weight:700;font-size:18px;margin-top:8px}
.price-note{font-size:12px;margin-top:14px;line-height:16px;width:150px}
.price-plain{font-family:'Montserrat',sans-serif;font-weight:700;font-size:23px;line-height:28px;width:150px}
.plan-body{position:absolute;left:228px;right:8px;top:16px}
.plan-body h3{font-family:'Montserrat',sans-serif;font-weight:700;font-size:24px;color:var(--ink);margin-bottom:8px;white-space:nowrap}
.plan-body ul{list-style:none}
.plan-body li{display:flex;align-items:center;gap:8px;font-size:15px;color:var(--ink);height:30px}
.tick{width:13px;height:13px;border-radius:50%;flex:none;display:flex;align-items:center;justify-content:center}
.tick.blue{background:var(--blue)}
.tick.salmon{background:var(--salmon)}
.plan-note{font-size:12px;line-height:19px;color:#666;margin-top:6px;width:200px}
.member-lead{left:0;top:1724px;width:1200px;text-align:center;font-size:21px;color:#333}
.member-special{left:0;top:1770px;width:1200px;text-align:center;font-weight:700;font-size:21px;color:var(--blue-text)}
.member-extra{left:0;top:1802px;width:1200px;text-align:center;font-size:16px;line-height:28px;color:#555}

/* classes */
.classes-title{left:0;top:2014px;width:1200px;text-align:center}
.classes-rule{left:431px;top:2082px;width:338px}
.class-photo{width:291px;height:253px}
.c1{background:linear-gradient(135deg,#5a4034,#a27a63 55%,#d7c8bd)}
.c2{background:linear-gradient(180deg,#7a8e6c,#b9b3a6 55%,#7e9a5f)}
.c3{background:linear-gradient(180deg,#8fa7c4,#c9b89a 45%,#e5e2dc)}
.c4{background:linear-gradient(135deg,#3b3c45,#8b98aa 50%,#cfd4db)}
.c5{background:linear-gradient(180deg,#6e6a5f,#948b7b 50%,#b3a894)}
.c6{background:linear-gradient(135deg,#d9cdbf,#6d7481 50%,#1c1f26)}

/* cafeteria */
.cafe{left:0;top:2731px;width:1200px;height:491px}
.cafe-title{left:143px;top:2810px}
.cafe-rule{left:143px;top:2878px;width:324px}
.cafe-copy{left:143px;top:2902px;width:405px;font-size:14px;line-height:31px;color:var(--muted)}
.cafe-btn{left:143px;top:3086px;width:163px}
.cafe-badge{left:572px;top:2955px;width:52px;height:52px;border-radius:50%;background:var(--white);border:3px solid var(--red)}

/* footer */
.footer-brand{left:146px;top:3290px}
.footer-brand .brand-dot{width:22px;height:22px}
.footer-brand .brand-name{font-size:29px}
.newsletter-title{left:653px;top:3275px;font-weight:700;font-size:21px;color:var(--ink)}
.newsletter-form{left:653px;top:3319px;width:402px;height:48px;border:1px solid #ccc;border-radius:24px;display:flex;align-items:center;justify-content:space-between;padding:0 4px 0 26px;font-size:13px;color:#666}
.newsletter-form span.submit{background:#111;color:var(--white);border-radius:20px;height:38px;width:96px;display:flex;align-items:center;justify-content:center;font-weight:700;font-size:15px}
.footer-divider{left:0;top:3408px;width:1200px;height:1px;background:#e8e8e8}
.footer-nav{left:0;top:3450px;width:1200px;display:flex;justify-content:center;gap:18px;font-size:19px;color:var(--ink)}
.footer-nav i{font-style:normal;color:#666}
.copyright{left:0;top:3494px;width:1200px;text-align:center;font-size:13px;color:#444}
.social{left:0;top:3534px;width:1200px;display:flex;justify-content:center;gap:12px}
.social span{width:20px;height:20px;border-radius:50%;background:#222}
</style>
</head>
<body>

<header class="abs site-header">
  <div class="abs brand header-brand"><span class="brand-dot"></span><span class="brand-name">BRASSWELL<br>TARGET SPORTS</span></div>
  <div class="abs phone-bar">
    <svg width="34" height="34" viewBox="0 0 34 34"><circle cx="17" cy="17" r="15" fill="none" stroke="#d2232a" stroke-width="2"/><path d="M12 9c1 0 2 3 2 4s-2 1-1 3 3 4 4 4 1-1 2-1 3 1 3 2-2 3-3 3c-5 0-10-6-10-11 0-2 2-4 3-4z" fill="#d2232a"/></svg>
    PHONE: <b>1 555 010 2424</b>
  </div>
  <nav class="abs main-nav">
    <span class="active">HOME</span><span>MEMBERSHIP</span><span>ABOUT US</span><span>CONTACT US</span><span>CLASSES</span><span>CAFE</span>
    <svg width="15" height="15" viewBox="0 0 15 15"><circle cx="6" cy="6" r="4.5" fill="none" stroke="#d2232a" stroke-width="2"/><path d="M9.5 9.5L14 14" stroke="#d2232a" stroke-width="2.5"/></svg>
  </nav>
</header>

<section class="abs hero">
  <div class="hero-photo" role="img" aria-label="Photo of a shooter in ear protection aiming a rifle down an indoor range lane"></div>
  <h1 class="abs hero-title">BRASSWELL<br>TARGET<br>SPORTS</h1>
  <div class="abs btn-outline-light">GET STARTED
    <svg width="14" height="14" viewBox="0 0 14 14"><circle cx="7" cy="7" r="7" fill="#fff"/><path d="M5 4l3 3-3 3" stroke="#222" stroke-width="2" fill="none"/></svg></div>
  <div class="abs carousel-arrow" style="left:66px"><svg width="12" height="12" viewBox="0 0 12 12"><path d="M8 1L3 6l5 5" stroke="#fff" stroke-width="2" fill="none"/></svg></div>
  <div class="abs carousel-arrow" style="left:1094px"><svg width="12" height="12" viewBox="0 0 12 12"><path d="M4 1l5 5-5 5" stroke="#fff" stroke-width="2" fill="none"/></svg></div>
  <div class="abs dots" style="top:518px"><span></span><span></span><span class="on"></span><span></span><span></span></div>
</section>

<svg class="abs hero-curve" width="1200" height="140" viewBox="0 0 1200 140">
  <path d="M0 20 Q600 160 1200 20 L1200 140 L0 140 Z" fill="#fff"/>
  <path d="M140 65 Q600 165 1060 65" fill="none" stroke="#d2232a" stroke-width="4"/>
</svg>
<div class="abs hero-badge"></div>

<section>
  <div class="abs welcome-emblem" role="img" aria-label="Large faint range emblem decoration"><div></div></div>
  <h2 class="abs welcome-title">WELCOME TO</h2>
  <p class="abs welcome-sub">BRASSWELL TARGET SPORTS</p>
  <div class="abs title-rule welcome-rule"></div>
  <p class="abs welcome-copy">We plan to start a family run state of the art indoor shooting range that is safe. We will foster an environment that allows men and women to come by themselves, feel comfortable, and are confident regardless of their experience level. We will hire staff based on guest service skills to focus on their overall experience.</p>
  <div class="abs btn-read welcome-btn">READ MORE
    <svg width="14" height="14" viewBox="0 0 14 14"><circle cx="7" cy="7" r="7" fill="#d2232a"/><path d="M5 4l3 3-3 3" stroke="#fff" stroke-width="2" fill="none"/></svg></div>
</section>

<svg class="abs membership-top" width="1200" height="66" viewBox="0 0 1200 66"><path d="M0 64 Q600 -60 1200 64 Z" fill="#f2f2f2"/></svg>
<section class="abs membership"></section>
<svg class="abs membership-bottom" width="1200" height="66" viewBox="0 0 1200 66"><path d="M0 1 Q600 125 1200 1 Z" fill="#f2f2f2"/></svg>

<h2 class="abs section-title membership-title"><b>OUR</b> <span>MEMBERSHIP</span></h2>
<div class="abs title-rule membership-rule"></div>

<article class="abs plan plan-yearly">
  <div class="price-panel blue">
    <div class="price-amount">$58</div>
    <div class="price-label">Initial Fee</div>
    <div class="price-note">(Waived if signed up prior to opening)</div>
  </div>
  <div class="plan-body">
    <h3>YEARLY</h3>
    <ul>
      <li><span class="tick blue"><svg width="8" height="8" viewBox="0 0 8 8"><path d="M1 4l2 2 4-4" stroke="#fff" stroke-width="1.6" fill="none"/></svg></span>Individual $300 a year</li>
      <li><span class="tick blue"><svg width="8" height="8" viewBox="0 0 8 8"><path d="M1 4l2 2 4-4" stroke="#fff" stroke-width="1.6" fill="none"/></svg></span>Dual $400 a year</li>
      <li><span class="tick blue"><svg width="8" height="8" viewBox="0 0 8 8"><path d="M1 4l2 2 4-4" stroke="#fff" stroke-width="1.6" fill="none"/></svg></span>Family $450 a year</li>
    </ul>
    <p class="plan-note">(Children are included up to age 26, and they do not need to live at home)</p>
  </div>
</article>

<article class="abs plan plan-monthly">
  <div class="price-panel salmon">
    <div class="price-plain">(no contract or obligation)</div>
  </div>
  <div class="plan-body">
    <h3>MONTH-MONTH</h3>
    <ul>
      <li><span class="tick salmon"><svg width="8" height="8" viewBox="0 0 8 8"><path d="M1 4l2 2 4-4" stroke="#fff" stroke-width="1.6" fill="none"/></svg></span>Individual $300 a year</li>
      <li><span class="tick salmon"><svg width="8" height="8" viewBox="0 0 8 8"><path d="M1 4l2 2 4-4" stroke="#fff" stroke-width="1.6" fill="none"/></svg></span>Dual $400 a year</li>
      <li><span class="tick salmon"><svg width="8" height="8" viewBox="0 0 8 8"><path d="M1 4l2 2 4-4" stroke="#fff" stroke-width="1.6" fill="none"/></svg></span>Family $450 a year</li>
    </ul>
    <p class="plan-note">(Children age up to 26, and they do not need to live at home)</p>
  </div>
</article>

<p class="abs member-lead">Members are allowed unlimited visits to the range</p>
<p class="abs member-special">SPECIAL BEFORE OPENING:</p>
<p class="abs member-extra">For every year purchased in advanced an additional 3 months will be given<br>Gunsmith will provide basic gunsmith services</p>

<section>
  <h2 class="abs section-title classes-title"><b>OUR</b> <span>CLASSES</span></h2>
  <div class="abs title-rule classes-rule"></div>
  <div class="abs class-photo c1" style="left:143px;top:2123px" role="img" aria-label="Photo of a student aiming a scoped rifle"></div>
  <div class="abs class-photo c2" style="left:455px;top:2123px" role="img" aria-label="Photo of a woman holding a paper target at an outdoor range"></div>
  <div class="abs class-photo c3" style="left:765px;top:2123px" role="img" aria-label="Photo of an instructor coaching a pistol grip outdoors"></div>
  <div class="abs class-photo c4" style="left:143px;top:2395px" role="img" aria-label="Photo of an instructor guiding a student's pistol stance"></div>
  <div class="abs class-photo c5" style="left:455px;top:2395px" role="img" aria-label="Photo of a group tactical drill on a dirt range"></div>
  <div class="abs class-photo c6" style="left:765px;top:2395px" role="img" aria-label="Photo of an instructor explaining a handgun to a student"></div>
</section>

<section class="abs cafe">
  <svg width="1200" height="491" viewBox="0 0 1200 491">
    <rect width="1200" height="491" fill="#fce9ea"/>
    <defs><linearGradient id="cafeTone" x1="0" y1="0" x2="1" y2="1"><stop offset="0" stop-color="#6b5a4b"/><stop offset=".5" stop-color="#b59c84"/><stop offset="1" stop-color="#3d3129"/></linearGradient></defs>
    <path d="M528 0 Q640 245 528 491 L1200 491 L1200 0 Z" fill="url(#cafeTone)" role="img" aria-label="Photo of a smiling barista serving a cup of coffee across the cafe counter"/>
  </svg>
</section>
<h2 class="abs section-title cafe-title"><b>OUR</b> <span>CAFETERIA</span></h2>
<div class="abs title-rule cafe-rule"></div>
<p class="abs cafe-copy">Brasswell Target Sports will have 22 individual room lanes: 5 lanes at 25 yard range, 13 lanes at 10 yard ranges, and 4 lanes at 5 yard range dedicated to an advanced live fire interactive graphic experience. We will also have a 22 foot wide open range for classes, corporate events, groups,</p>
<div class="abs btn-read cafe-btn">READ MORE
  <svg width="14" height="14" viewBox="0 0 14 14"><circle cx="7" cy="7" r="7" fill="#d2232a"/><path d="M5 4l3 3-3 3" stroke="#fff" stroke-width="2" fill="none"/></svg></div>
<div class="abs cafe-badge"></div>

<footer>
  <div class="abs brand footer-brand"><span class="brand-dot"></span><span class="brand-name">BRASSWELL<br>TARGET SPORTS</span></div>
  <h3 class="abs newsletter-title">SIGN UP NEWSLETTER</h3>
  <div class="abs newsletter-form"><span>Enter Email</span><span class="submit">SIGN UP</span></div>
  <div class="abs footer-divider"></div>
  <nav class="abs footer-nav"><span>HOME</span><i>/</i><span>MEMBERSHIP</span><i>/</i><span>ABOUT US</span><i>/</i><span>CONTACT US</span><i>/</i><span>CLASSES</span><i>/</i><span>CAFE</span></nav>
  <p class="abs copyright">© 2019 Brasswell Target Sports.All Rights Reserved</p>
  <div class="abs social"><span aria-label="Social link"></span><span aria-label="Social link"></span><span aria-label="Social link"></span><span aria-label="Social link"></span></div>
</footer>

</body>
</html>
```